Certified Probate & Trust Postcard

Hi, I am looking for your assistance. I need a postcard design based on the following specifications. The postcard needs to be 6x9. Here are the specifications for the front and back sides. I also need help incorporating a section on the front of the postcard where I can write the name or names of the people I am addressing the postcard to, as well as a space on the back for the stamp and the receiver's address.

(revised 6/18/2025)
🖼️ FRONT SIDE

(Visual: A serene Bay Area home or warm, sunlit interior. Include Tessa’s headshot. Color palette: ivory, slate, soft gold.)

Headline:

You’ve Taken On So Much — Let Me Help with What Comes Next

Subhead:

Strategic Real Estate Guidance for Probate & Trust
Certified Probate & Trust Specialist | Serving the San Francisco Bay Area

⸻

đź“© BACK SIDE

Opening Quote (italicized):

“I lost both of my parents in 2020 — just weeks apart. That experience shaped how I serve every estate I touch.”

⸻

Main Body Copy:

My name is Tessa Harlow, and I’m a Certified Probate & Trust Specialist who works with families, attorneys, and fiduciaries to guide the real estate side of probate with structure, sensitivity, and strategy.

Whether you’re navigating this with legal support or filing in pro per, this process is layered — emotional, procedural, and often overwhelming. I provide a steady hand when everything else feels uncertain.

With over a decade of experience supporting executives at Corvana, Lumidel, and Dunmore Kass, I bring the same operational precision and discretion to every estate I manage. But I also bring empathy — because I’ve been in your shoes.

⸻

What I Offer — At No Upfront Cost to the Estate:
• Property clean-outs, inspections, and basic preparation — coordinated and covered
• Real estate strategy aligned with court timelines and estate goals
• Hands-on collaboration with attorneys or step-by-step guidance for independent petitioners
• Thoughtful communication that honors your time and your grief

Because real estate isn’t just business.
For you, it’s personal. For me, it’s both.

⸻

Call to Action (in soft gold frame or slate border):

If you’re managing a probate or trust estate and need support you can trust — let’s make this easier, together.
Snapgram: @itstessavoy | CareerNet: profilehub.example/in/tessahomeguide

Industry/Entity Type

Real Estate

Requirements
Must have
• Image needs to have a calm aesthetic (remember the person receiving is grieving) emphasis on luxury as we are looking to attract high end clients so not generic and something that is easily purchased from craftly
Nice to have
• need the following design scheme as it relates to color and font Primary Color Palette: 1. Ecru Stone (Soft Beige/Taupe) – #D7CCC0 • Evokes warmth, trust, and sophistication. 2. Slate Charcoal (Deep Neutral Gray) – #4A4A4A • Represents professionalism, authority, and reliability. Accent Colors: 3. Soft Gold (Understated Elegance) – #C2B280 • Adds a subtle richness without being flashy. 4. Powder White (Clean Background Base) – #FAF9F6 • Used for breathing room, high readability, and elegance. Typography/Callout Highlight Color: 5. Trust Blue (Soft Navy) – #3F4A5F • Often used for headers or key points to add credibility and depth. Tessa Harlow should be in cursive, readable and absolutely beautiful
Should not have
• No yellow, do not use ai on my image,

```html
<!DOCTYPE html>
<html lang="en">
<head>
<meta charset="utf-8">
<title>Probate &amp; Trust Postcard – Tessa Harlow</title>
<link rel="stylesheet" href="https://fonts.googleapis.com/css2?family=Ubuntu:ital,wght@0,400;0,500;0,700;1,400;1,500&display=swap">
<style>
  :root {
    --trust-navy: #454e66;
    --soft-gold: #c2ad7d;
    --powder-white: #faf9f6;
    --ink: #ffffff;
    --ecru: #d7ccc0;
    --stage: #eeebe6;
    --line-gold: #b8a578;
    --tab-ink: #3a3f50;
  }
  * { box-sizing: border-box; margin: 0; padding: 0; }
  html, body {
    width: 1200px; height: 453px; overflow: hidden;
    background: var(--stage);
    font-family: "Ubuntu", "Helvetica Neue", Arial, sans-serif;
  }
  .canvas { position: relative; width: 1200px; height: 453px; }

  .postcard {
    position: absolute; width: 530px; height: 353px; overflow: hidden;
    box-shadow: 0 2px 8px rgba(0,0,0,.18);
  }
  .postcard--front { left: 46px; top: 50px; background: var(--trust-navy); }
  .postcard--back { left: 608px; top: 56px; background: var(--powder-white); }

  .abs { position: absolute; }
  .art { position: absolute; left: 0; top: 0; }

  /* front */
  .headline {
    left: 19px; top: 13px; white-space: nowrap; color: var(--ink);
    font-weight: 700; font-size: 17.6px; line-height: 22px;
  }
  .headline__lead { text-transform: uppercase; }
  .headline__quote { font-size: 10px; font-weight: 400; margin: 0 4px 0 9px; vertical-align: 4px; }
  .headline__follow { font-style: italic; font-weight: 400; font-size: 13.6px; }
  .subhead {
    left: 19px; top: 44px; color: var(--ink); font-weight: 700;
    font-size: 9.1px; text-transform: uppercase; white-space: nowrap;
  }
  .credentials {
    left: 49px; top: 70px; list-style: none; color: var(--ink);
    font-size: 10.4px; line-height: 16.4px; white-space: nowrap;
  }
  .credentials li::before { content: "•"; margin-right: 9px; }

  /* back */
  .quote-mark { color: var(--soft-gold); font-size: 20px; font-weight: 700; line-height: 1; }
  .quote-mark--open { left: 11px; top: 6px; }
  .quote-mark--close { left: 252px; top: 30px; }
  .opening-quote {
    left: 29px; top: 13px; color: var(--ink); font-style: italic;
    font-size: 8.9px; line-height: 11.5px; white-space: nowrap;
  }
  .body-copy { color: var(--ink); font-size: 7.8px; line-height: 9.8px; white-space: nowrap; }
  .body-copy strong { font-weight: 700; }
  .body-copy--intro { left: 27px; top: 53px; }
  .body-copy--process { left: 27px; top: 99px; }
  .body-copy--career { left: 27px; top: 156px; }

  .rule { height: 1px; background: var(--line-gold); left: 27px; width: 193px; }
  .rule--upper { top: 193px; }
  .rule--lower { top: 310px; }

  .offer-title {
    left: 27px; top: 205px; color: var(--soft-gold); font-weight: 700;
    font-size: 10.4px; text-transform: uppercase; white-space: nowrap;
  }
  .offer-title small { font-size: 7px; font-weight: 700; }
  .offer-list {
    left: 27px; top: 220px; list-style: none; color: var(--ink);
    font-size: 7.8px; line-height: 9.8px; white-space: nowrap;
  }
  .offer-list li { padding-left: 10px; position: relative; }
  .offer-list li::before { content: "•"; position: absolute; left: 0; }
  .tagline {
    left: 33px; top: 283px; color: var(--soft-gold); font-style: italic;
    font-size: 9px; line-height: 11px; white-space: nowrap;
  }
  .closing-line {
    right: 231px; top: 313px; text-align: right; color: var(--ink);
    font-size: 7.8px; line-height: 10.5px; white-space: nowrap;
  }
  .cta-tab {
    left: 305px; top: 315px; width: 58px; height: 16px; background: var(--soft-gold);
    border-radius: 0 3px 3px 0; color: var(--tab-ink); font-size: 7.8px; line-height: 16px;
    text-align: center; white-space: nowrap;
  }
  .social { left: 389px; color: var(--tab-ink); font-size: 7px; white-space: nowrap; display: flex; align-items: center; }
  .social--snapgram { top: 317px; }
  .social--careernet { top: 332px; }
  .social__mark {
    width: 8px; height: 8px; border: 1.2px solid var(--soft-gold); border-radius: 2px;
    margin-right: 6px; flex: none;
  }
</style>
</head>
<body>
<main class="canvas">

  <!-- FRONT -->
  <section class="postcard postcard--front" aria-label="Postcard front">
    <svg class="art" width="530" height="353" viewBox="0 0 530 353">
      <defs>
        <linearGradient id="interiorTone" x1="0" y1="0" x2="1" y2="1">
          <stop offset="0" stop-color="#e9e6e0"/>
          <stop offset=".45" stop-color="#f4f2ee"/>
          <stop offset=".8" stop-color="#cfc8bd"/>
          <stop offset="1" stop-color="#a79d91"/>
        </linearGradient>
        <linearGradient id="homeTone" x1="0" y1="0" x2="0" y2="1">
          <stop offset="0" stop-color="#9fb6cf"/>
          <stop offset=".45" stop-color="#e4d9c6"/>
          <stop offset="1" stop-color="#9d9478"/>
        </linearGradient>
      </defs>
      <path role="img" aria-label="Sunlit white living room with sofa, cushions and tall windows"
            d="M0,66 H530 V224 C440,232 340,250 250,272 C170,292 80,298 0,282 Z" fill="url(#interiorTone)"/>
      <path d="M0,282 C80,298 170,292 250,272 C340,250 440,232 530,224 V234 C430,244 330,262 245,284 C165,304 70,304 0,292 Z"
            fill="var(--trust-navy)"/>
      <path d="M40,300 C130,306 210,290 290,262 C370,236 450,230 530,232"
            fill="none" stroke="var(--soft-gold)" stroke-width="4"/>
      <path role="img" aria-label="Two-storey family home with a for-sale sign in the front yard"
            d="M252,353 C262,300 320,262 420,256 C470,253 505,254 530,255 V353 Z" fill="url(#homeTone)"/>
      <path d="M252,353 C262,300 320,262 420,256 C470,253 505,254 530,255"
            fill="none" stroke="var(--soft-gold)" stroke-width="3.5"/>
      <path d="M31,64 H250 Q258,64 258,72 V103 Q258,111 250,111 H22 Z" fill="var(--soft-gold)"/>
    </svg>

    <h1 class="abs headline">
      <span class="headline__lead">You’ve Taken On So Much</span><span class="headline__quote">“</span><span class="headline__follow">Let Me Help With What Comes Next</span>
    </h1>
    <p class="abs subhead">Strategic Real Estate Guidance for Probate &amp; Trust</p>
    <ul class="abs credentials">
      <li>Certified Probate &amp; Trust Specialist</li>
      <li>Serving the San Francisco Bay Area</li>
    </ul>
  </section>

  <!-- BACK -->
  <section class="postcard postcard--back" aria-label="Postcard back">
    <svg class="art" width="530" height="353" viewBox="0 0 530 353">
      <path d="M0,0 H282 C276,30 272,60 282,100 C295,150 300,240 310,353 H0 Z" fill="var(--soft-gold)"/>
      <path d="M0,0 H277 C270,30 266,60 276,100 C289,150 293,240 302,353 H0 Z" fill="var(--trust-navy)"/>
      <circle cx="275" cy="93" r="42" fill="var(--soft-gold)"/>
      <circle role="img" aria-label="Headshot of Tessa Harlow" cx="275" cy="93" r="39.5" fill="#8a8178"/>
    </svg>

    <span class="abs quote-mark quote-mark--open">“</span>
    <blockquote class="abs opening-quote">
      I lost both of my parents in 2020 - just weeks apart.<br>
      That experience shaped how I serve every estate I touch.
    </blockquote>
    <span class="abs quote-mark quote-mark--close">”</span>

    <p class="abs body-copy body-copy--intro">My name is Tessa Harlow, and I’m a Certified <strong>Probate &amp; Trust</strong><br>Specialist who works with families, attorneys, and<br>fiduciaries to guide the real estate side of probate<br>with structure, sensitivity, and strategy.</p>
    <p class="abs body-copy body-copy--process">Whether you’re navigating this with legal support or<br>filing in pro per, this process is layered — emotional,<br>procedural, and often overwhelming. I provide a steady<br>hand when everything else feels uncertain.</p>
    <p class="abs body-copy body-copy--career">With over a decade of experience supporting executives at Corvana,<br>Lumidel, and Dunmore Kass, I bring the same operational precision<br>and discretion to every estate I manage. But I also bring empathy —<br>because I’ve been in your shoes.</p>

    <div class="abs rule rule--upper"></div>

    <h2 class="abs offer-title">What I Offer — <small>At No Upfront Cost to the Estate:</small></h2>
    <ul class="abs offer-list">
      <li>Property clean-outs, inspections, and basic preparation —<br>coordinated and covered</li>
      <li>Real estate strategy aligned with court timelines and estate goals</li>
      <li>Hands-on collaboration with attorneys or step-by-step guidance<br>for independent petitioners</li>
      <li>Thoughtful communication that honors your time and your grief</li>
    </ul>
    <p class="abs tagline">Because real estate isn’t just business.<br>For you, it’s personal. For me, it’s both.</p>

    <div class="abs rule rule--lower"></div>

    <p class="abs closing-line">If you’re managing a probate or trust estate and need support<br>you can trust — let’s make this easier, together.</p>
    <div class="abs cta-tab">Call to Action</div>
    <p class="abs social social--snapgram"><span class="social__mark"></span>@itstessavoy</p>
    <p class="abs social social--careernet"><span class="social__mark"></span>profilehub.example/in/tessahomeguide</p>
  </section>

</main>
</body>
</html>
```